Business Card Design Project

We are looking for an eye catching, unique business card design that incorporates our logo and a photo of the mortgage associate.

We will need to have our business address included (could be on the back of the card), as well as the mortgage associate's information:

Name
Position
Phone
Email

Logo attached.

Target Market(s)

Clients (people purchasing homes, renewing existing mortgages, or refinancing existing mortgages)
Referral sources such as realtors, financial advisors, relocation specialists, real estate lawyers...

Industry/Entity Type

Business

Requirements
Must have
• Logo
Name and contact information of associate
Address of brokerage
Nice to have
• Photo of the agent

```html
<!DOCTYPE html>
<html lang="en">
<head>
<meta charset="UTF-8">
<title>Keystone Home Lending – Business Card</title>
<link href="https://fonts.googleapis.com/css2?family=Tinos&family=Montserrat:wght@500&display=swap" rel="stylesheet">
<style>
  :root {
    --ink-light: #ffffff;
    --ink-dark: #2e2e30;
    --accent: #a8261c;
    --cyan: #3fd6da;
    --teal: #2bb9d2;
    --blue: #1b5fe0;
    --deep-blue: #0c2fc4;
    --mist: #b9d7da;
  }
  * { margin: 0; padding: 0; box-sizing: border-box; }
  html, body { width: 1200px; height: 686px; overflow: hidden; background: #ffffff; }
  .card {
    position: relative;
    width: 1200px;
    height: 686px;
    overflow: hidden;
    font-family: "Tinos", "Times New Roman", serif;
    color: var(--ink-light);
  }
  .card__backdrop {
    position: absolute;
    inset: 0;
    background:
      radial-gradient(ellipse 520px 300px at 120px 640px, rgba(185,215,218,0.95), rgba(185,215,218,0) 70%),
      radial-gradient(ellipse 420px 260px at 260px 230px, rgba(63,214,218,0.9), rgba(63,214,218,0) 75%),
      radial-gradient(ellipse 380px 220px at 980px 560px, rgba(12,47,196,0.7), rgba(12,47,196,0) 75%),
      radial-gradient(ellipse 460px 260px at 760px 40px, rgba(12,47,196,0.75), rgba(12,47,196,0) 75%),
      linear-gradient(100deg, var(--teal) 0%, var(--cyan) 30%, var(--blue) 62%, var(--teal) 80%, var(--blue) 100%);
  }
  .address {
    position: absolute;
    left: 34px;
    top: 66px;
  }
  .address__pin { position: absolute; left: 0; top: 0; width: 90px; height: 86px; }
  .address__title {
    position: absolute;
    left: 101px;
    top: 14px;
    font-size: 43px;
    font-weight: 400;
    white-space: nowrap;
  }
  .address__line {
    position: absolute;
    left: 101px;
    width: 354px;
    border-bottom: 2px solid var(--ink-light);
  }
  .address__line--first { top: 146px; }
  .address__line--second { top: 230px; }

  .contact { position: absolute; left: 626px; top: 146px; }
  .contact__row { position: absolute; left: 0; height: 60px; width: 530px; }
  .contact__label { position: absolute; left: 0; top: 0; font-size: 50px; line-height: 60px; white-space: nowrap; }
  .contact__colon { position: absolute; top: 0; font-size: 50px; line-height: 60px; }
  .contact__line { position: absolute; border-bottom: 2px solid var(--ink-light); top: 55px; }
  .contact__row--name { top: 0; }
  .contact__row--position { top: 103px; }
  .contact__row--phone { top: 206px; }
  .contact__row--email { top: 309px; }

  .brand {
    position: absolute;
    left: 34px;
    top: 520px;
    width: 440px;
    height: 140px;
    color: var(--ink-dark);
  }
  .brand__name {
    display: flex;
    align-items: center;
    gap: 12px;
    font-size: 40px;
    white-space: nowrap;
  }
  .brand__mark { width: 26px; height: 26px; background: var(--accent); flex: none; }
  .brand__tagline {
    position: absolute;
    left: 46px;
    top: 108px;
    font-family: "Montserrat", Arial, sans-serif;
    font-weight: 500;
    font-size: 14.5px;
    letter-spacing: 0.8px;
    white-space: nowrap;
  }
</style>
</head>
<body>
  <div class="card">
    <div class="card__backdrop" role="img" aria-label="Abstract flowing background of cyan, teal and deep blue light streaks"></div>

    <section class="address">
      <svg class="address__pin" viewBox="0 0 90 86" aria-hidden="true">
        <defs>
          <radialGradient id="pin-head" cx="0.35" cy="0.3" r="0.75">
            <stop offset="0" stop-color="#e9ffff"/>
            <stop offset="0.5" stop-color="#7ee6ec"/>
            <stop offset="1" stop-color="#2aa6b8"/>
          </radialGradient>
        </defs>
        <line x1="44" y1="44" x2="50" y2="74" stroke="#8a9aa0" stroke-width="4" stroke-linecap="round"/>
        <ellipse cx="38" cy="26" rx="32" ry="24" fill="url(#pin-head)"/>
        <ellipse cx="47" cy="42" rx="14" ry="7" fill="#3bb3c2"/>
      </svg>
      <h2 class="address__title">Business Address</h2>
      <div class="address__line address__line--first"></div>
      <div class="address__line address__line--second"></div>
    </section>

    <section class="contact">
      <div class="contact__row contact__row--name">
        <span class="contact__label">Name</span>
        <span class="contact__colon" style="left:172px">:</span>
        <span class="contact__line" style="left:192px;width:328px"></span>
      </div>
      <div class="contact__row contact__row--position">
        <span class="contact__label">Position:</span>
        <span class="contact__line" style="left:190px;width:328px"></span>
      </div>
      <div class="contact__row contact__row--phone">
        <span class="contact__label">Phone</span>
        <span class="contact__colon" style="left:163px">:</span>
        <span class="contact__line" style="left:184px;width:330px"></span>
      </div>
      <div class="contact__row contact__row--email">
        <span class="contact__label">Email</span>
        <span class="contact__colon" style="left:172px">:</span>
        <span class="contact__line" style="left:192px;width:328px"></span>
      </div>
    </section>

    <section class="brand">
      <div class="brand__name">
        <span class="brand__mark"></span>
        <span>Keystone Home Lending</span>
      </div>
      <p class="brand__tagline">Home loans shaped around the way you live</p>
    </section>
  </div>
</body>
</html>
```